Residential & commercial cleaning business

Looking for Brazilian colors, green/blue/yellow.
Name of business is “Marla’s Cleaning”.
Second side of card will be for ‘confirming customer next appointment date/time.
Want to include in description…residential & commercial cleaning, experienced, highly recommended, reasonable rates, free estimates, Marla’sCleaningVT@brightmop.com, Londonderry, NH, Call today at 802.517.3946.

```html
<!DOCTYPE html>
<html lang="en">
<head>
<meta charset="utf-8">
<title>Marla’s Cleaning – Business Card</title>
<link rel="stylesheet" href="https://fonts.googleapis.com/css2?family=Poppins:wght@400;700&family=Montserrat:wght@800&display=swap">
<style>
  :root {
    --bg: #2a2a2a;
    --card: #ffffff;
    --green: #0a9a48;
    --yellow: #ffdd00;
    --ink: #1e1e1e;
  }
  * { box-sizing: border-box; margin: 0; padding: 0; }
  html, body { width: 1200px; height: 880px; overflow: hidden; background: var(--bg); }
  .sheet {
    width: 1200px; height: 880px;
    display: flex; flex-direction: column; align-items: center; justify-content: center; gap: 48px;
  }
  .card {
    position: relative; width: 640px; height: 366px;
    background: var(--card); border-radius: 22px; overflow: hidden;
  }
  .brand {
    display: flex; align-items: center; gap: 12px;
    font-family: "Poppins", sans-serif; font-weight: 700; color: var(--green); white-space: nowrap;
  }
  .brand-dot { width: 18px; height: 18px; border-radius: 50%; background: var(--yellow); flex: none; }
  .card-front .brand {
    position: absolute; inset: 0; justify-content: center; font-size: 46px;
  }
  .card-back .brand { position: absolute; left: 34px; top: 146px; font-size: 28px; }
  .services {
    position: absolute; right: 30px; top: 30px; list-style: none;
    font-family: "Poppins", sans-serif; font-size: 17px; line-height: 24px; color: var(--ink); text-align: right;
  }
  .services li { display: flex; justify-content: flex-end; align-items: center; gap: 10px; }
  .services svg { width: 14px; height: 14px; fill: var(--yellow); flex: none; }
  .appointment-title {
    position: absolute; right: 58px; top: 160px;
    font-family: "Montserrat", sans-serif; font-weight: 800; font-size: 16px; color: var(--green);
  }
  .appointment-line {
    position: absolute; left: 250px; right: 26px; top: 188px;
    display: flex; align-items: flex-end; gap: 6px;
    font-family: "Poppins", sans-serif; font-size: 15px; line-height: 18px; color: var(--ink);
  }
  .appointment-line .blank { flex: 1; border-bottom: 2px dotted var(--ink); height: 16px; }
  .appointment-line .blank-short { flex: 1.2; }
  .swoosh { position: absolute; inset: 0; }
  .call {
    position: absolute; right: 40px; bottom: 34px;
    font-family: "Montserrat", sans-serif; font-weight: 800; font-size: 18px; color: var(--yellow);
  }
  .call .phone { font-family: "Poppins", sans-serif; font-weight: 400; margin-left: 10px; }
</style>
</head>
<body>
<main class="sheet">
  <section class="card card-front">
    <div class="brand"><span class="brand-dot"></span>Marla’s Cleaning</div>
  </section>

  <section class="card card-back">
    <svg class="swoosh" viewBox="0 0 640 366" aria-hidden="true">
      <path d="M0,304 C200,266 420,240 630,226 C440,252 260,292 80,366 L0,366 Z" fill="var(--yellow)"/>
      <path d="M122,366 C280,302 450,258 640,240 L640,366 Z" fill="var(--green)"/>
    </svg>
    <div class="brand"><span class="brand-dot"></span>Marla’s Cleaning</div>
    <ul class="services">
      <li>residential &amp; commercial cleaning<svg viewBox="0 0 10 10"><path d="M5 0 6 4 10 5 6 6 5 10 4 6 0 5 4 4Z"/></svg></li>
      <li>experienced<svg viewBox="0 0 10 10"><path d="M5 0 6 4 10 5 6 6 5 10 4 6 0 5 4 4Z"/></svg></li>
      <li>highly recommended<svg viewBox="0 0 10 10"><path d="M5 0 6 4 10 5 6 6 5 10 4 6 0 5 4 4Z"/></svg></li>
      <li>reasonable rates<svg viewBox="0 0 10 10"><path d="M5 0 6 4 10 5 6 6 5 10 4 6 0 5 4 4Z"/></svg></li>
      <li>free estimates<svg viewBox="0 0 10 10"><path d="M5 0 6 4 10 5 6 6 5 10 4 6 0 5 4 4Z"/></svg></li>
    </ul>
    <div class="appointment-title">NEXT APPOINTMENT</div>
    <div class="appointment-line">
      <span class="blank blank-short"></span><span>AT</span><span class="blank"></span><span>AM/PM</span>
    </div>
    <div class="call">CALL TODAY<span class="phone">802.517.3946.</span></div>
  </section>
</main>
</body>
</html>
```